Kestrel Homes Australia Business Card

We need a Business Card design for our new start up company.
A unique model designed to address Australia’s growing housing affordability problem has been launched. More than half of Australians are being priced out of the property market and have resigned themselves to the fact that they may never be able to afford a home.
We have developed a unique Algorithm that allows people to get into property and reverse this trend of domination by the property investors in this country. The first of its kind model facilitates connecting people to lending facilities that do not require them to have the finance combined under the purchase contract.
Ownership is shared with a second-tier investor, made up of either family or friends if not, Kestrel Homes Australia will provide a mini property investor enabling thousands of people the opportunity to buy a home, which they otherwise thought was not possible.
Kestrel Homes Australia is addressing housing affordability for families and individuals, giving every Australian looking to buy a home the opportunity to enter the property market to live in or invest.
Under our unique model, there is no combined finance, and individuals are assessed for their percentage portion of the property only. “A unique feature of our product is it is based around the strategies used for property investment. I have developed a unique Algorithm that enables the Home buyer to purchase 60% of a property, while Kestrel Homes Australia facilitates a second-tier investor to buy the other 40%. The Algorithm locks the investor in place and enables the home buyer to stairway to full ownership. The investment is secured against real property.
Please refer to our website www.kestrelhomes.com.au for inspiration.
Also please find attached our logo.
Any further directions please ask.
Cheers Marcus
Industry/Entity Type
Real Estate
Contact Information for Business Card
Marcus Thorley
CEO
Mobile 0400 615 272
www.kestrelhomes.com.au
Email: marcus@kestrelhomes.com.au
Colors
Designer to choose colors to be used in the design.
Look and feel

```html
<!DOCTYPE html>
<html lang="en">
<head>
<meta charset="utf-8">
<title>Kestrel Homes Australia – Business Card</title>
<link rel="stylesheet" href="https://fonts.googleapis.com/css2?family=Montserrat:wght@500;700&family=Roboto+Condensed:wght@400;700&family=Roboto:wght@400&display=swap">
<style>
  :root {
    --backdrop: #2a2a2a;
    --card-white: #f2f2f2;
    --brand-green: #2e9a3e;
    --brand-green-light: #45a847;
    --brand-blue: #02a3c7;
    --tagline-green: #3f7f12;
    --text-light: #ffffff;
  }
  * { margin: 0; padding: 0; box-sizing: border-box; }
  html, body { width: 1200px; height: 960px; overflow: hidden; }
  body { background: var(--backdrop); position: relative; font-family: "Roboto", Arial, sans-serif; }

  .card {
    position: absolute;
    width: 600px;
    height: 343px;
    overflow: hidden;
  }
  .card--front { left: 314px; top: 113px; background: var(--card-white); }
  .card--back { left: 311px; top: 472px; background: var(--brand-blue); color: var(--text-light); }

  .front-swoosh { position: absolute; inset: 0; width: 600px; height: 343px; }

  .brand-name {
    position: absolute;
    left: 0; right: 0;
    text-align: center;
    font-family: "Montserrat", Arial, sans-serif;
    font-weight: 700;
    white-space: nowrap;
  }
  .brand-tagline {
    position: absolute;
    left: 0; right: 0;
    text-align: center;
    font-family: "Montserrat", Arial, sans-serif;
    font-weight: 500;
    white-space: nowrap;
  }
  .card--front .brand-name { top: 106px; font-size: 22px; color: var(--brand-blue); }
  .card--front .brand-tagline { top: 137px; font-size: 13px; color: var(--tagline-green); }

  .person { position: absolute; left: 35px; top: 269px; color: var(--text-light); }
  .person__name { font-family: "Roboto Condensed", Arial, sans-serif; font-weight: 700; font-size: 21px; letter-spacing: 0.2px; }
  .person__role { font-family: "Roboto Condensed", Arial, sans-serif; font-size: 15px; margin-top: 3px; }

  .contact-list {
    position: absolute;
    right: 28px;
    top: 264px;
    list-style: none;
    color: var(--text-light);
    font-size: 14px;
    text-align: right;
  }
  .contact-list li { display: flex; justify-content: flex-end; align-items: center; gap: 5px; height: 20px; }
  .contact-list svg { width: 13px; height: 13px; flex: none; }

  .card--back .brand-name { top: 180px; font-size: 29px; }
  .card--back .brand-tagline { top: 219px; font-size: 16px; }
  .back-url {
    position: absolute;
    left: 0; right: 0; top: 295px;
    text-align: center;
    font-size: 14px;
    letter-spacing: 6px;
  }
</style>
</head>
<body>

<section class="card card--front">
  <svg class="front-swoosh" viewBox="0 0 600 343" aria-hidden="true">
    <defs>
      <linearGradient id="greenFill" x1="0" y1="0" x2="0" y2="1">
        <stop offset="0" stop-color="#238f36"/>
        <stop offset="1" stop-color="#45a847"/>
      </linearGradient>
    </defs>
    <path d="M0,190 C20,150 50,128 92,115 C58,140 58,185 90,205 C170,255 390,250 550,170 C575,155 590,135 600,118 L600,343 L0,343 Z" fill="url(#greenFill)"/>
    <path d="M66,186 C85,230 190,252 300,249 C405,246 490,215 552,170 C490,208 405,238 300,241 C190,244 92,224 66,186 Z" fill="#02a3c7"/>
  </svg>

  <div class="brand-name">Kestrel Homes Australia</div>
  <div class="brand-tagline">Helping Every Buyer Own a Home</div>

  <div class="person">
    <div class="person__name">MARCUS THORLEY</div>
    <div class="person__role">CEO</div>
  </div>

  <ul class="contact-list">
    <li>0400615272
      <svg viewBox="0 0 13 13" aria-hidden="true"><rect x="3" y="0.5" width="7" height="12" rx="1.2" fill="none" stroke="#fff" stroke-width="1.2"/><circle cx="6.5" cy="10.4" r="0.8" fill="#fff"/></svg>
    </li>
    <li>marcus@kestrelhomes.com.au
      <svg viewBox="0 0 13 13" aria-hidden="true"><rect x="0.5" y="2.5" width="12" height="8" fill="#fff"/><path d="M0.5,2.5 L6.5,7 L12.5,2.5" fill="none" stroke="#3a9f42" stroke-width="1"/></svg>
    </li>
    <li>www.kestrelhomes.com.au
      <svg viewBox="0 0 13 13" aria-hidden="true"><circle cx="6.5" cy="6.5" r="6" fill="#fff"/><path d="M3,4 C5,3 6,5 5,7 C4,9 6,10 7,12 M8,1.5 C8,4 10,4 12,5" fill="none" stroke="#3a9f42" stroke-width="1.3"/></svg>
    </li>
  </ul>
</section>

<section class="card card--back">
  <div class="brand-name">Kestrel Homes Australia</div>
  <div class="brand-tagline">Helping Every Buyer Own a Home</div>
  <div class="back-url">www.kestrelhomes.com.au</div>
</section>

</body>
</html>
```